Flyer-Design für Werkstatt-Umzug
Vielen lieben Dank für das tolle Design, sowie die schnelle Bearbeitung. Auch nach dem Zuschlag ein toller Service.
Zielgruppe
Wir sind eine kleine Kfz-Werkstatt und ziehen nun um. Dazu soll ein Info-Flyer ausgelegt werden und mit in Rechnungen & Briefe. Zielgruppe sind neben der deutschen Kundschaft, auch viele dänische Kunden.
Aufgabenstellung
Wir dachten einen zweiseitigen Flyer (DIN lang), vorne Deutsch, hinten Dänisch. Wir dachten an folgenden Text:
Deutsch: Ab Januar 2018 begrüßen wir Sie in unserer neuen Werkstatt
Homepage www.kfz-technik-olmer.de
Dänisch: Januar 2018 er alle hjertelig velkommen i hvores nye værksted:

```html
<!DOCTYPE html>
<html lang="da">
<head>
<meta charset="utf-8">
<title>Flyer – Vi flytning</title>
<link href="https://fonts.googleapis.com/css2?family=Arimo:wght@400;700&display=swap" rel="stylesheet">
<style>
  :root {
    --page-bg: #222222;
    --paper: #ffffff;
    --brand-red: #e60000;
    --brand-red-dark: #c80000;
    --ink: #111111;
    --figure-light: #f2f2f2;
    --figure-shade: #c9c9c9;
    --map-green: #b9d9a4;
    --map-beige: #efe6d4;
  }
  html, body {
    margin: 0;
    width: 1184px;
    height: 1200px;
    overflow: hidden;
    background: var(--page-bg);
    font-family: "Arimo", Arial, sans-serif;
  }
  .flyer {
    position: absolute;
    left: 32px;
    top: 312px;
    width: 1250px;
    height: 642px;
    background: var(--paper);
    overflow: hidden;
    transform: scale(0.896);
    transform-origin: 0 0;
  }
  .header-band {
    position: absolute;
    left: 0; top: 43px;
    width: 1250px; height: 151px;
    background: linear-gradient(90deg, var(--brand-red) 0%, var(--brand-red) 60%, var(--brand-red-dark) 85%, var(--brand-red) 100%);
  }
  .flag-cross-v {
    position: absolute; left: 1151px; top: 47px;
    width: 25px; height: 143px; background: var(--paper);
  }
  .flag-cross-h {
    position: absolute; left: 1094px; top: 109px;
    width: 156px; height: 23px; background: var(--paper);
  }
  .service-icons {
    position: absolute; left: 32px; top: 81px;
    display: flex; gap: 7px;
  }
  .service-icon {
    width: 72px; height: 72px; border-radius: 50%;
    background: var(--paper);
  }
  .web-address {
    position: absolute; right: 162px; top: 57px;
    color: var(--paper); font-weight: 700; font-size: 19px;
  }
  .headline {
    position: absolute; right: 155px; top: 94px;
    margin: 0; color: var(--paper); font-weight: 700;
    font-size: 63px; letter-spacing: 2px; line-height: 1;
  }
  .mover-illustration {
    position: absolute; left: 290px; top: 67px;
    width: 335px; height: 545px;
    border-radius: 48% 48% 30% 30%;
    background: radial-gradient(ellipse at 45% 40%, var(--figure-light) 0%, var(--figure-shade) 70%, transparent 72%);
  }
  .helpers-illustration {
    position: absolute; left: 994px; top: 387px;
    width: 226px; height: 215px;
    background: radial-gradient(ellipse at 50% 50%, #e6e6e6 0%, #d4b58a 45%, transparent 70%);
  }
  .location-map {
    position: absolute; left: -70px; top: 308px;
    width: 430px; height: 430px; border-radius: 50%;
    border: 6px solid var(--brand-red);
    box-sizing: border-box;
    background: linear-gradient(135deg, var(--map-green) 0%, var(--map-beige) 55%, var(--map-green) 100%);
  }
  .date {
    position: absolute; left: 620px; width: 450px; top: 222px;
    margin: 0; text-align: center;
    color: var(--brand-red); font-weight: 700; font-size: 61px; line-height: 1;
  }
  .welcome {
    position: absolute; left: 610px; width: 480px; top: 310px;
    margin: 0; text-align: center;
    color: var(--ink); font-size: 36px; line-height: 37px;
  }
  .address {
    position: absolute; left: 620px; width: 440px; top: 412px;
    margin: 0; text-align: center; font-style: normal;
    color: var(--ink); font-size: 36px; line-height: 41px;
  }
  .corner-mark {
    position: absolute; right: 0; bottom: 0;
    width: 31px; height: 30px; background: var(--brand-red);
  }
</style>
</head>
<body>
  <section class="flyer">
    <div class="header-band"></div>
    <div class="flag-cross-h"></div>
    <div class="flag-cross-v"></div>

    <div class="service-icons">
      <div class="service-icon" role="img" aria-label="Service-Symbol Reparatur"></div>
      <div class="service-icon" role="img" aria-label="Service-Symbol Karosserie"></div>
      <div class="service-icon" role="img" aria-label="Service-Symbol Lackierung"></div>
    </div>

    <div class="web-address">www.olmer-werkstatt.de</div>
    <h1 class="headline">VI FLYTNING...</h1>

    <div class="location-map" role="img" aria-label="Kartenausschnitt mit dem neuen Werkstatt-Standort"></div>
    <div class="mover-illustration" role="img" aria-label="3D-Figur trägt einen Umzugskarton"></div>
    <div class="helpers-illustration" role="img" aria-label="Zwei 3D-Figuren mit Kartons und Sackkarre"></div>

    <p class="date">Januar 2018</p>
    <p class="welcome">er alle hjertelig velkommen<br>i hvores nye værksted</p>
    <address class="address">Am Werkhof 12<br>24939 Nordhafen<br>Tyskland</address>

    <div class="corner-mark"></div>
  </section>
</body>
</html>
```